Construction Company Facebook Banner

We are a small residential building company, building mostly new homes, renovations, extensions. our social media needs an uplift to look more professional.
I have no photos I wish to use in the banner as of yet however I have included the company logo, and the business card design which has some details.
I would like something simple but professional.
The banner does not need to have email, phone number, services provided etc. all of this is available on the facebook page itself. Something simple and clean please.
Industry/Entity Type
Construction
Requirements
Should not have
- Images of people, QR Code

```html
<!DOCTYPE html>
<html lang="en">
<head>
<meta charset="utf-8">
<title>Brightfield Builders – Facebook Cover</title>
<link href="https://fonts.googleapis.com/css2?family=Rubik:wght@500;600&family=Roboto:wght@400&family=Archivo+Black&display=swap" rel="stylesheet">
<style>
  :root{
    --brand-green:#31b24b;
    --white:#ffffff;
    --badge-grey:#7a7a7a;
    --badge-ring:#d9d9d9;
    --page-bg:#efefef;
    --sky-top:#c9cfd8;
    --roof-mid:#a89c8c;
    --ground:#6e5a4e;
  }
  html,body{margin:0;padding:0;width:1200px;height:1200px;overflow:hidden;background:var(--page-bg);}
  .cover{
    position:absolute;left:40px;top:382px;width:1120px;height:436px;overflow:hidden;
    box-shadow:0 18px 40px rgba(0,0,0,.18);
  }
  .cover__photo{
    position:absolute;right:0;top:0;width:560px;height:100%;
    background:linear-gradient(180deg,var(--sky-top) 0%,#b9b3aa 30%,var(--roof-mid) 60%,var(--ground) 100%);
  }
  .cover__shape{position:absolute;left:0;top:0;width:100%;height:100%;}
  .brand{
    position:absolute;left:214px;top:94px;display:flex;align-items:center;gap:10px;
    color:var(--white);font-family:"Rubik",sans-serif;font-weight:500;font-size:22px;line-height:1;
  }
  .brand__mark{width:18px;height:18px;background:var(--white);flex:none;}
  .headline{
    position:absolute;left:213px;top:140px;margin:0;color:var(--white);
    font-family:"Rubik",sans-serif;font-weight:600;font-size:42px;line-height:43px;
  }
  .services{position:absolute;left:218px;top:278px;margin:0;padding:0;list-style:none;
    display:grid;grid-template-columns:148px 148px;grid-auto-rows:27.5px;
    color:var(--white);font-family:"Roboto",sans-serif;font-size:18px;}
  .services li{display:flex;align-items:center;gap:10px;}
  .services svg{width:19px;height:19px;flex:none;}
  .badge{
    position:absolute;left:607px;top:245px;width:150px;height:150px;border-radius:50%;
    background:var(--badge-grey);border:5px solid var(--white);box-sizing:border-box;
    box-shadow:0 0 0 2px var(--badge-ring);
    display:flex;align-items:center;justify-content:center;
  }
  .badge__text{
    transform:rotate(-20deg);color:var(--white);font-family:"Archivo Black",sans-serif;
    font-size:22px;line-height:22px;text-align:center;letter-spacing:.5px;
  }
</style>
</head>
<body>
  <section class="cover">
    <div class="cover__photo" role="img" aria-label="Photo of a newly built gable-roof carport with steel trusses beside a brick home under a cloudy sky"></div>
    <svg class="cover__shape" viewBox="0 0 1620 630" preserveAspectRatio="none" aria-hidden="true">
      <path d="M0 0 H862 C1120 150 1190 430 842 630 H0 Z" fill="var(--white)" stroke="var(--white)" stroke-width="30"/>
      <path d="M0 0 H862 C1120 150 1190 430 842 630 H0 Z" fill="var(--brand-green)"/>
    </svg>

    <div class="brand">
      <span class="brand__mark" aria-hidden="true"></span>
      <span class="brand__name">Brightfield Builders</span>
    </div>

    <h1 class="headline">Professional<br>Construction<br>Services</h1>

    <ul class="services">
      <li><svg viewBox="0 0 24 24"><path d="M20 11.5A8.5 8.5 0 1 1 15.5 4" fill="none" stroke="#fff" stroke-width="2.4" stroke-linecap="round"/><path d="M7.5 11.5l4 4L22 4.5" fill="none" stroke="#fff" stroke-width="2.6" stroke-linecap="round" stroke-linejoin="round"/></svg>Service 01</li>
      <li><svg viewBox="0 0 24 24"><path d="M20 11.5A8.5 8.5 0 1 1 15.5 4" fill="none" stroke="#fff" stroke-width="2.4" stroke-linecap="round"/><path d="M7.5 11.5l4 4L22 4.5" fill="none" stroke="#fff" stroke-width="2.6" stroke-linecap="round" stroke-linejoin="round"/></svg>Service 04</li>
      <li><svg viewBox="0 0 24 24"><path d="M20 11.5A8.5 8.5 0 1 1 15.5 4" fill="none" stroke="#fff" stroke-width="2.4" stroke-linecap="round"/><path d="M7.5 11.5l4 4L22 4.5" fill="none" stroke="#fff" stroke-width="2.6" stroke-linecap="round" stroke-linejoin="round"/></svg>Service 02</li>
      <li><svg viewBox="0 0 24 24"><path d="M20 11.5A8.5 8.5 0 1 1 15.5 4" fill="none" stroke="#fff" stroke-width="2.4" stroke-linecap="round"/><path d="M7.5 11.5l4 4L22 4.5" fill="none" stroke="#fff" stroke-width="2.6" stroke-linecap="round" stroke-linejoin="round"/></svg>Service 05</li>
      <li><svg viewBox="0 0 24 24"><path d="M20 11.5A8.5 8.5 0 1 1 15.5 4" fill="none" stroke="#fff" stroke-width="2.4" stroke-linecap="round"/><path d="M7.5 11.5l4 4L22 4.5" fill="none" stroke="#fff" stroke-width="2.6" stroke-linecap="round" stroke-linejoin="round"/></svg>Service 03</li>
      <li><svg viewBox="0 0 24 24"><path d="M20 11.5A8.5 8.5 0 1 1 15.5 4" fill="none" stroke="#fff" stroke-width="2.4" stroke-linecap="round"/><path d="M7.5 11.5l4 4L22 4.5" fill="none" stroke="#fff" stroke-width="2.6" stroke-linecap="round" stroke-linejoin="round"/></svg>Service 06</li>
    </ul>

    <div class="badge">
      <div class="badge__text">GREAT<br>RANGE!<br>GREAT<br>PRICES!</div>
    </div>
  </section>
</body>
</html>
```